Attractive WP design (Velmora) for our textile production and trading business

We need a design for our new website. We would like it to be based on the WP theme Velmora.

1) Description of the business
Kandrel GmbH is a textile company that is specialized in production and trading of high-quality cotton fabrics/products.

We…
• design and develop
• weave (incl. special weaving/embroidery technique)
• shear
• finish the products (Logo printing, packing)

Our products are…
• Swiss Ghutra
• Shemagh (=Yashmagh) (https://www.tervastoff.ch/en/competence/clothing-textiles/clothing-for-arab-and-african-markets/#210)
• Desdasha’s (https://www.tervastoff.ch/en/competence/clothing-textiles/clothing-for-arab-and-african-markets/#210)
• Emmas and Shawls
Emmas are traditional head coverings worn by Muslim man in Sudan. The cloth of exactly 5 yards in length is winded around the head like a turban. The cloth can be plain white, have a decorative trim or be colored. There are also matching scarfs.
• Brocade/Damask
• Atiku
• Kemora Voile (https://pomlatrade.com/products/kemora-3?_pos=2&_sid=98a067e86&_ss=r)
--> Please see attached pictures of the different fabrics and products

2) Target audience and users
• (Foreign) wholesalers interested in trading with Kandrel

3) Goals of the website
Kandrel has been a family-run textile business for 17 years with no web presence. The majority of our historical sales have been based on pre-existing relationships or word-of-mouth connections. Now, we seek to diversify our customer base. For this, we want our first website/online presence in order to:

• Enable foreign wholesalers to discover Kandrel as a supplier of Swiss quality fabric;
• Showcase both our current specific product line as well as our general manufacturing capabilities for new custom products;
• Enable inquiries/orders by interested parties

4) Design wishes
The design should reflect our high quality textiles. The design should be clean, inviting, friendly and professional. Colors can be chosen freely. Pictures should not overload sites but support our goal to attract and inspire future buyers.

If you have any questions, please reach out to us!

• the site will be multilingual (german/english/possibly french)

```html
<!DOCTYPE html>
<html lang="en">
<head>
<meta charset="utf-8">
<title>Kandrel – Cotton Fabrics</title>
<link rel="stylesheet" href="https://fonts.googleapis.com/css2?family=Montserrat:wght@500;600;700&family=Lato:wght@400;700&display=swap">
<style>
:root{
  --ink:#1d1d1d;
  --nav:#333;
  --accent:#2b4f8a;
  --light:#f5f5f5;
  --line:#d6d6d6;
  --footer:#2e2e2e;
  --footer-text:#e6e6e6;
  --white:#fff;
}
*{margin:0;padding:0;box-sizing:border-box}
html,body{width:1200px;height:3819px;overflow:hidden;background:var(--white)}
body{position:relative;font-family:"Lato",sans-serif;color:var(--ink)}
.abs{position:absolute}
.head-font{font-family:"Montserrat",sans-serif}

/* header */
.brand{left:111px;top:22px;font-family:"Montserrat",sans-serif;font-weight:700;font-size:34px;color:var(--ink);display:flex;align-items:center;gap:10px}
.brand .dot{width:14px;height:14px;border-radius:50%;background:var(--ink)}
.topline{right:120px;top:20px;font-size:17px;color:var(--ink);display:flex;align-items:center;gap:8px}
.topline svg{width:14px;height:14px;fill:var(--accent)}
.lang{margin-left:24px;font-weight:700}
.nav{top:68px;left:485px;display:flex;font-family:"Montserrat",sans-serif;font-weight:500;font-size:17px;color:var(--nav)}
.nav span{position:absolute;white-space:nowrap}
.nav .active{color:var(--accent)}

/* hero */
.hero{left:0;top:111px;width:1200px;height:558px;background:linear-gradient(100deg,#6d6a66 0%,#9a9690 28%,#b7b4af 45%,#7d4a6a 62%,#8e2249 75%,#3f3f72 100%)}
.hero-title{left:108px;top:238px;font-family:"Montserrat",sans-serif;font-weight:600;font-size:66px;color:var(--white);letter-spacing:1px}
.hero-sub{left:111px;top:323px;font-size:21px;line-height:32px;color:var(--white)}
.btn-light{background:var(--white);color:var(--ink);font-family:"Montserrat",sans-serif;font-weight:500;display:flex;align-items:center;justify-content:center}
.order{left:111px;top:415px;width:187px;height:64px;font-size:19px}

/* products */
.section-title{width:1200px;left:0;text-align:center;font-family:"Montserrat",sans-serif;font-weight:500;font-size:37px}
.tile{overflow:hidden}
.tile .shade{position:absolute;left:0;right:0;bottom:0;height:45%;background:linear-gradient(rgba(0,0,0,0),rgba(0,0,0,.45))}
.tile .label{position:absolute;left:0;right:0;bottom:28px;text-align:center;color:var(--white);font-family:"Montserrat",sans-serif;font-weight:600;font-size:22px}
.btn-dark{background:var(--ink);color:var(--white);font-family:"Montserrat",sans-serif;font-weight:600;display:flex;align-items:center;justify-content:center}
.view{left:520px;top:1873px;width:159px;height:52px;font-size:17px}

/* enquiry */
.enquiry-bg{left:0;top:2005px;width:667px;height:518px;background:var(--light)}
.enquiry-photo{left:667px;top:2005px;width:420px;height:518px;background:linear-gradient(150deg,#c59b5b 0%,#efe6d8 30%,#f6f4f0 55%,#8aa5c8 80%,#b2532c 100%)}
.enquiry-title{left:109px;top:2067px;font-family:"Montserrat",sans-serif;font-weight:500;font-size:37px}
.field{background:var(--white);border:1px solid var(--line);font-size:16px;color:#777;padding:14px 15px}
.send{left:111px;top:2399px;width:116px;height:52px;font-size:17px}

/* about */
.about-photo{left:0;top:2523px;width:600px;height:470px;background:linear-gradient(135deg,#8d8f94 0%,#e9e9ea 35%,#f6f6f6 55%,#c9c9cc 75%,#6d6f74 100%)}
.about-panel{left:600px;top:2523px;width:600px;height:470px;background:var(--accent)}
.about-title{left:668px;top:2578px;font-family:"Montserrat",sans-serif;font-weight:500;font-size:37px;color:var(--white)}
.about-text{left:668px;top:2642px;width:430px;font-size:16.5px;line-height:26.5px;color:#e6ebf3}
.about-text p+p{margin-top:27px}
.more{left:669px;top:2858px;width:147px;height:53px;font-size:17px}

/* services */
.service-icon{width:118px;height:118px;border-radius:14px;background:linear-gradient(135deg,#dfe6f1,#b9c7de)}
.service-label{width:300px;text-align:center;font-family:"Montserrat",sans-serif;font-weight:500;font-size:21px;color:#444}

/* footer */
.footer{left:0;top:3405px;width:1200px;height:414px;background:var(--footer)}
.foot-brand{left:111px;top:3510px;font-family:"Montserrat",sans-serif;font-weight:700;font-size:62px;color:var(--white)}
.vat{left:111px;top:3656px;font-size:20px;color:var(--white)}
.foot-head{font-family:"Montserrat",sans-serif;font-weight:600;font-size:20px;color:var(--white)}
.links{left:470px;top:3520px;font-size:16.5px;line-height:31px;color:var(--footer-text)}
.contact{font-size:16.5px;line-height:24px;color:var(--footer-text)}
.contact svg{position:absolute;left:-30px;top:4px;width:16px;height:16px;fill:var(--white)}
.divider{left:111px;top:3727px;width:978px;height:1px;background:#555}
.copyright{left:111px;top:3762px;font-size:16.5px;color:var(--footer-text)}
.social{width:48px;height:48px;border:2px solid var(--white);border-radius:50%;color:var(--white);font-family:"Montserrat",sans-serif;font-weight:600;font-size:13px;display:flex;align-items:center;justify-content:center}
</style>
</head>
<body>

<header>
  <div class="abs brand">Kandrel<span class="dot"></span></div>
  <div class="abs topline">
    <svg viewBox="0 0 24 24"><path d="M6.6 10.8a15.1 15.1 0 0 0 6.6 6.6l2.2-2.2a1 1 0 0 1 1-.25 11.4 11.4 0 0 0 3.6.57 1 1 0 0 1 1 1V20a1 1 0 0 1-1 1A17 17 0 0 1 3 4a1 1 0 0 1 1-1h3.5a1 1 0 0 1 1 1c0 1.25.2 2.45.57 3.57a1 1 0 0 1-.25 1z"/></svg>
    <span>+41 71 555 20 87</span><span>&nbsp;|&nbsp;</span>
    <svg viewBox="0 0 24 24"><path d="M2 5h20v14H2z M2 5l10 8 10-8" fill="var(--accent)"/></svg>
    <span>info@kandrel-textil.ch</span>
    <span class="lang">Eng ⌄</span>
  </div>
  <nav class="abs nav">
    <span class="active" style="left:0">HOME</span>
    <span style="left:89px">ABOUT US</span>
    <span style="left:215px">SERVICES</span>
    <span style="left:335px">PRODUCTS</span>
    <span style="left:469px">CONTACT</span>
    <svg style="position:absolute;left:590px;top:2px" width="16" height="16" viewBox="0 0 16 16"><circle cx="6.5" cy="6.5" r="5" fill="none" stroke="#333" stroke-width="2"/><path d="M10.5 10.5l4 4" stroke="#333" stroke-width="2"/></svg>
  </nav>
</header>

<section>
  <div class="abs hero" role="img" aria-label="Photo of a woman in a magenta silk headscarf on a city street"></div>
  <h1 class="abs hero-title">KANDREL</h1>
  <p class="abs hero-sub">Specialized in production and trading of<br>high-quality cotton fabrics/products</p>
  <div class="abs btn-light order">ORDER NOW!</div>
</section>

<section>
  <h2 class="abs section-title" style="top:736px">OUR PRODUCTS</h2>

  <div class="abs tile" style="left:111px;top:820px;width:482px;height:331px;background:linear-gradient(160deg,#6f6f6f,#c8c8c8 45%,#e8e8e8 70%,#9b9b9b)" role="img" aria-label="Photo of folded white Swiss ghutra cloth"><div class="shade"></div><div class="label">Swiss Ghutra</div></div>
  <div class="abs tile" style="left:607px;top:820px;width:482px;height:331px;background:linear-gradient(150deg,#f1e3e4,#d8324a 40%,#f4eced 60%,#c01f36)" role="img" aria-label="Photo of red and white checked shemagh fabric"><div class="shade"></div><div class="label">Shemagh (=Yashmagh)</div></div>

  <div class="abs tile" style="left:111px;top:1166px;width:316px;height:310px;background:linear-gradient(160deg,#f2eeea,#ddd6cf 50%,#b9a89a)" role="img" aria-label="Photo of men wearing white desdashas and red headscarves"><div class="shade"></div><div class="label">Desdasha’s</div></div>
  <div class="abs tile" style="left:442px;top:1166px;width:316px;height:310px;background:linear-gradient(160deg,#9fb9c8,#c34a5a 35%,#5a3a2e 65%,#9fb6c4)" role="img" aria-label="Photo of a woman wearing a colourful patterned head wrap"><div class="shade"></div><div class="label">Emmas and Shawls</div></div>
  <div class="abs tile" style="left:773px;top:1166px;width:316px;height:310px;background:linear-gradient(160deg,#dfe5ef,#c3cede 50%,#a9b7cb)" role="img" aria-label="Photo of pale blue brocade damask fabric"><div class="shade"></div><div class="label">Brocade/Damask</div></div>

  <div class="abs tile" style="left:111px;top:1490px;width:482px;height:333px;background:linear-gradient(110deg,#c9c6c0,#f2f0ec 40%,#dcd8d2 70%,#bdb8b1)" role="img" aria-label="Photo of white atiku fabric drapes"><div class="shade"></div><div class="label">Atiku</div></div>
  <div class="abs tile" style="left:607px;top:1490px;width:482px;height:333px;background:radial-gradient(ellipse at 50% 60%,#6fb6c6 0%,#8fc7d2 30%,#eeeeee 60%)" role="img" aria-label="Photo of a turquoise checked voile scarf on a mannequin"><div class="shade"></div><div class="label">Kemora Voile</div></div>

  <div class="abs btn-dark view">VIEW MORE</div>
</section>

<section>
  <div class="abs enquiry-bg"></div>
  <div class="abs enquiry-photo" role="img" aria-label="Close-up photo of threads on a weaving loom"></div>
  <h2 class="abs enquiry-title">ENQUIRY FORM</h2>
  <div class="abs field" style="left:111px;top:2143px;width:255px;height:48px">Name:</div>
  <div class="abs field" style="left:377px;top:2143px;width:256px;height:48px">Email:</div>
  <div class="abs field" style="left:111px;top:2204px;width:255px;height:48px">Phone:</div>
  <div class="abs field" style="left:377px;top:2204px;width:256px;height:48px">Address:</div>
  <div class="abs field" style="left:111px;top:2264px;width:522px;height:108px">Message:</div>
  <div class="abs btn-dark send">SEND</div>
</section>

<section>
  <div class="abs about-photo" role="img" aria-label="Photo of white thread spools on a spinning machine"></div>
  <div class="abs about-panel"></div>
  <h2 class="abs about-title">ABOUT KANDREL</h2>
  <div class="abs about-text">
    <p>Kandrel GmbH is a textile company that is specialized in production and trading of high-quality cotton fabrics/ products.</p>
    <p>Nemo enim ipsam voluptatem quia voluptas sit arnatur aut odit aut fugit, sed quia consequuntur magni dolore silos qui ratione voluptatem sequi nesc.</p>
  </div>
  <div class="abs btn-light more">READ MORE</div>
</section>

<section>
  <h2 class="abs section-title" style="top:3066px">WHAT WE DO</h2>
  <div class="abs service-icon" style="left:162px;top:3162px" role="img" aria-label="Icon for design and development"></div>
  <div class="abs service-icon" style="left:439px;top:3162px" role="img" aria-label="Icon for special weaving"></div>
  <div class="abs service-icon" style="left:647px;top:3162px" role="img" aria-label="Icon for shearing"></div>
  <div class="abs service-icon" style="left:905px;top:3162px" role="img" aria-label="Icon for logo printing and packing"></div>
  <div class="abs service-label" style="left:71px;top:3300px">Design and Develop</div>
  <div class="abs service-label" style="left:348px;top:3300px">Special Weaving</div>
  <div class="abs service-label" style="left:556px;top:3300px">Shear</div>
  <div class="abs service-label" style="left:814px;top:3300px">Logo printing &amp; Packing</div>
</section>

<footer>
  <div class="abs footer"></div>
  <div class="abs foot-brand">Kandrel</div>
  <div class="abs vat">CHE-482.309.617 MWST</div>

  <div class="abs foot-head" style="left:470px;top:3473px">Qucik Links</div>
  <div class="abs links">Home<br>About us<br>Services<br>Products<br>Contact</div>

  <div class="abs foot-head" style="left:701px;top:3473px">Contact Information</div>
  <div class="abs contact" style="left:728px;top:3520px">
    <svg viewBox="0 0 24 24"><path d="M12 2a7 7 0 0 0-7 7c0 5 7 13 7 13s7-8 7-13a7 7 0 0 0-7-7zm0 9.5A2.5 2.5 0 1 1 12 6.5a2.5 2.5 0 0 1 0 5z"/></svg>
    Lindengasse 14<br>CH – 9010 Hallwil<br>Switzerland
  </div>
  <div class="abs contact" style="left:732px;top:3617px">
    <svg viewBox="0 0 24 24"><path d="M6.6 10.8a15.1 15.1 0 0 0 6.6 6.6l2.2-2.2a1 1 0 0 1 1-.25 11.4 11.4 0 0 0 3.6.57 1 1 0 0 1 1 1V20a1 1 0 0 1-1 1A17 17 0 0 1 3 4a1 1 0 0 1 1-1h3.5a1 1 0 0 1 1 1c0 1.25.2 2.45.57 3.57a1 1 0 0 1-.25 1z"/></svg>
    +41 71 555 20 87
  </div>
  <div class="abs contact" style="left:736px;top:3664px">
    <svg viewBox="0 0 24 24"><path d="M2 5h20v14H2z"/><path d="M2 5l10 8 10-8" fill="none" stroke="#2e2e2e" stroke-width="2"/></svg>
    info@kandrel-textil.ch
  </div>

  <div class="abs divider"></div>
  <div class="abs copyright">Copyright © 2021, Kandrel. All rights reserved.</div>
  <div class="abs social" style="left:928px;top:3750px">FB</div>
  <div class="abs social" style="left:984px;top:3750px">TW</div>
  <div class="abs social" style="left:1041px;top:3750px">IN</div>
</footer>

</body>
</html>
```